Meridian Rest Supply Needs Business Card

Looking for a very nice looking business card. Creative but not extravagant. We sell beds and pillows across the U.S. and need something professional but catchy. I have attached the logo.

Name : Dale Fenwick
Title : President
Phone : (800) 417-2964
Email: sleep@quorvana.com
Website: www.quorvana.com

Can be single-sided or double-sided
horizontal or vertical

Can use Blues/Greys

Target Market(s)

Mass Market

Industry/Entity Type

Retail

Contact Information for Business Card

Name : Dale Fenwick
Title : President
Phone : (800) 417-2964
Email: sleep@quorvana.com
Website: www.quorvana.com

Requirements
Must have
• Clean, Modern, Smooth
• Can use Blues/Greys
• On the other side without the information - have something simple like www.quorvana.com or our logo
Nice to have
• Surprise me
Should not have
• Nothing crazy, nothing cluttered

```html
<!DOCTYPE html>
<html lang="en">
<head>
<meta charset="utf-8">
<title>Meridian Rest Supply – Business Card</title>
<link rel="stylesheet" href="https://fonts.googleapis.com/css2?family=Poppins:wght@400;500&display=swap">
<style>
  :root {
    --backdrop: #c6e7dd;
    --card-center: #00adec;
    --card-edge: #0a78b4;
    --band-dark: #0b4f97;
    --band-mid: #1560b0;
    --rule-light: #5fd0f7;
    --name-blue: #18a3e2;
    --title-grey: #6f6f6f;
    --white: #ffffff;
    --avatar-fill: #13a2e3;
  }
  * { box-sizing: border-box; margin: 0; padding: 0; }
  html, body {
    width: 1200px; height: 1200px; overflow: hidden;
    background: var(--backdrop);
    font-family: "Poppins", Arial, sans-serif;
  }
  .card {
    position: absolute; left: 100px; top: 315px;
    width: 1000px; height: 570px;
    border-radius: 52px; overflow: hidden;
    background: radial-gradient(ellipse 60% 75% at 62% 48%, var(--card-center) 0%, #0596d6 45%, var(--card-edge) 100%);
    color: var(--white);
  }
  .brand {
    position: absolute; left: 0; right: 0; top: 95px; height: 120px;
    display: flex; align-items: center; justify-content: center;
  }
  .brand-name {
    font-weight: 400; font-size: 60px; line-height: 1;
    letter-spacing: 1px;
    color: var(--white);
  }
  .contact-list {
    position: absolute; left: 54px; top: 318px;
    list-style: none;
  }
  .contact-item {
    display: flex; align-items: center;
    height: 46px;
    font-weight: 400; font-size: 28px;
  }
  .contact-icon { width: 30px; height: 30px; margin-right: 18px; flex: none; }
  .name-tab {
    position: absolute; left: 530px; right: -10px; top: 332px; height: 122px;
    border-radius: 61px 0 0 61px;
    background: linear-gradient(90deg, #0b86c6, #0d7fbd);
    padding: 6px 0 6px 6px;
  }
  .name-tab-inner {
    height: 100%;
    border-radius: 55px 0 0 55px;
    border: 3px solid var(--rule-light);
    border-right: none;
    background: var(--white);
    display: flex; align-items: center;
    padding-left: 10px;
  }
  .avatar {
    width: 92px; height: 92px; border-radius: 50%;
    background: var(--avatar-fill);
    border: 4px solid var(--white);
    box-shadow: 0 0 0 3px var(--avatar-fill);
    flex: none; margin-right: 16px;
  }
  .person-name {
    font-weight: 500; font-size: 40px; line-height: 1;
    letter-spacing: 2px; color: var(--name-blue);
  }
  .person-title {
    font-weight: 400; font-size: 26px; line-height: 1.1;
    color: var(--title-grey);
  }
  .footer-rule {
    position: absolute; left: 0; right: 0; top: 504px; height: 4px;
    background: var(--rule-light);
  }
  .footer-band {
    position: absolute; left: 0; right: 0; top: 508px; bottom: 0;
    background: linear-gradient(90deg, var(--band-dark) 0%, var(--band-mid) 50%, var(--band-dark) 100%);
    display: flex; align-items: center; justify-content: center;
    font-weight: 400; font-size: 33px; color: var(--white);
  }
</style>
</head>
<body>
  <main class="card">
    <div class="brand">
      <div class="brand-name">Meridian Rest Supply</div>
    </div>

    <ul class="contact-list">
      <li class="contact-item">
        <svg class="contact-icon" viewBox="0 0 30 30" aria-hidden="true">
          <path d="M3 11c0-4 6-6 12-6s12 2 12 6l-1 3h-5l-1-3c-3-1-7-1-10 0l-1 3H4z" fill="#fff"/>
          <path d="M7 15h16l3 11H4z" fill="#fff"/>
          <circle cx="15" cy="20" r="3.2" fill="#0a8fcf"/>
        </svg>
        (800) 417-2964
      </li>
      <li class="contact-item">
        <svg class="contact-icon" viewBox="0 0 30 30" aria-hidden="true">
          <rect x="2" y="7" width="26" height="17" fill="#fff"/>
          <path d="M2 7l13 10L28 7M2 24l10-9M28 24L18 15" stroke="#0a8fcf" stroke-width="1.8" fill="none"/>
        </svg>
        sleep@quorvana.com
      </li>
      <li class="contact-item">
        <svg class="contact-icon" viewBox="0 0 30 30" aria-hidden="true">
          <g fill="none" stroke="#fff" stroke-width="1.6">
            <circle cx="15" cy="15" r="11"/>
            <ellipse cx="15" cy="15" rx="5" ry="11"/>
            <path d="M4 15h22M6 9h18M6 21h18M15 4v22"/>
          </g>
        </svg>
        www.quorvana.com
      </li>
    </ul>

    <div class="name-tab">
      <div class="name-tab-inner">
        <div class="avatar" role="img" aria-label="Profile portrait placeholder"></div>
        <div class="name-block">
          <div class="person-name">Dale Fenwick</div>
          <div class="person-title">President</div>
        </div>
      </div>
    </div>

    <div class="footer-rule"></div>
    <div class="footer-band">www.quorvana.com</div>
  </main>
</body>
</html>
```